Scholarly Pathways - educational consulting

I am beginning an educational consultation business - focusing on Tribal (Native American Indian) Communities, but will work with anyone. I have work experience in K-12 and Higher Education. Special Education - transition from school to work. Advising and facilitating with academic skills in higher education. I have a BS - Special Education, Masters - Educational Administration and working on a PhD in Higher Education. Also completing PMB approved certification as an Academic Life Coach

Target Market(s)

K12 college bound students and parents, Kinfolk Crossings college bound students and families, special education college bound students and parents

Industry/Entity Type

Business

Contact Information for Business Card

Marnie Odell Fenwick. PO Box 417, Cushing, OK 74023. (918) 555-0293. marnie@scholarlypathways.example

Requirements
Must have
• Scholarly Pathways is the name of the business - Kinfolk Crossings is a focus area
Nice to have
• Tourquoise would be nice. I do not have a logo yet

```html
<!DOCTYPE html>
<html lang="en">
<head>
<meta charset="utf-8">
<title>Scholarly Pathways — Business Card</title>
<link href="https://fonts.googleapis.com/css2?family=Cinzel:wght@400;600&family=Montserrat:wght@400;500;600&display=swap" rel="stylesheet">
<style>
  :root {
    --stage: #2e2e30;
    --card-white: #ffffff;
    --card-black: #0b0b0c;
    --pink: #e0217a;
    --turquoise: #1ba6d9;
    --ink: #1a1a1a;
    --muted: #555555;
  }
  * { box-sizing: border-box; margin: 0; padding: 0; }
  html, body {
    width: 1200px; height: 801px; overflow: hidden;
    background: var(--stage);
    font-family: "Montserrat", Arial, sans-serif;
  }
  .sheet {
    width: 1200px; height: 801px;
    display: flex; align-items: center; justify-content: center; gap: 44px;
  }
  .card {
    position: relative;
    width: 540px; height: 309px;
    overflow: hidden;
    box-shadow: 0 14px 30px rgba(0,0,0,.45);
  }

  /* ---------- front ---------- */
  .card--front { background: var(--card-white); }
  .brand {
    position: absolute; left: 18px; top: 96px; width: 220px;
    text-align: center;
  }
  .brand__mark {
    display: flex; align-items: center; justify-content: center; gap: 8px;
  }
  .brand__dot {
    width: 14px; height: 14px; border-radius: 50%; background: var(--pink);
  }
  .brand__name {
    font-weight: 600; font-size: 15px; color: var(--turquoise);
    white-space: nowrap;
  }
  .brand__tagline {
    margin-top: 12px;
    font-size: 5.5px; letter-spacing: 1.8px; color: var(--ink);
    text-transform: uppercase; white-space: nowrap;
  }
  .details {
    position: absolute; left: 246px; top: 26px; right: 14px;
    padding-left: 9px;
    border-left: 1.5px solid var(--pink);
  }
  .details__name {
    font-family: "Cinzel", Georgia, serif; font-weight: 400;
    font-size: 15px; letter-spacing: 2.2px; color: var(--pink);
    text-transform: uppercase; line-height: 1; white-space: nowrap;
  }
  .details__cred {
    margin-top: 5px;
    font-size: 5.2px; letter-spacing: .2px; color: var(--muted);
    text-transform: uppercase; line-height: 1.6; white-space: nowrap;
  }
  .contact { margin-top: 12px; }
  .contact__row {
    display: flex; align-items: center; gap: 6px;
    font-size: 13px; color: var(--ink); line-height: 1.3; white-space: nowrap;
  }
  .contact__row--small { font-size: 10px; }
  .contact__icon { width: 11px; height: 14px; flex: none; }
  .band {
    position: absolute; left: 0; right: 0; bottom: 0; height: 40px;
    background: var(--card-black);
    padding: 9px 16px 0;
    font-size: 5.6px; letter-spacing: .4px; text-transform: uppercase;
    line-height: 1.9; white-space: nowrap;
  }
  .band__line { color: #ffffff; }
  .band__line--accent { color: var(--pink); }
  .band__notch {
    position: absolute; right: 40px; bottom: 40px;
    width: 14px; height: 9px;
  }

  /* ---------- back ---------- */
  .card--back {
    background: var(--card-black);
    display: flex; flex-direction: column; align-items: center; justify-content: center;
  }
  .card--back .brand__mark { gap: 10px; }
  .card--back .brand__dot { width: 20px; height: 20px; }
  .card--back .brand__name { font-size: 20px; }
  .back__name {
    margin-top: 26px;
    font-family: "Cinzel", Georgia, serif;
    font-size: 22px; letter-spacing: 5px; color: var(--pink);
    text-transform: uppercase; white-space: nowrap;
  }
  .back__tagline {
    margin-top: 4px;
    font-size: 7px; letter-spacing: 2.4px; color: #ffffff;
    text-transform: uppercase;
  }
</style>
</head>
<body>
<main class="sheet">

  <section class="card card--front" aria-label="Business card, front">
    <div class="brand">
      <div class="brand__mark">
        <span class="brand__dot"></span>
        <span class="brand__name">Scholarly Pathways</span>
      </div>
      <p class="brand__tagline">Educational Consultation Business</p>
    </div>

    <div class="details">
      <h1 class="details__name">Marnie Odell Fenwick</h1>
      <p class="details__cred">Masters - Educational Administration | PhD in Higher Education<br>BS - Special Education</p>
      <div class="contact">
        <p class="contact__row">
          <svg class="contact__icon" viewBox="0 0 11 14" aria-hidden="true">
            <rect x="1" y="0.5" width="9" height="13" rx="1.5" fill="none" stroke="#e0217a" stroke-width="1.2"/>
            <line x1="4" y1="11.5" x2="7" y2="11.5" stroke="#e0217a" stroke-width="1.2"/>
          </svg>
          918.555.0293
        </p>
        <p class="contact__row contact__row--small">
          <svg class="contact__icon" viewBox="0 0 11 14" aria-hidden="true">
            <path d="M5.5 2 L10.5 7 H9 V12 H2 V7 H0.5 Z" fill="#e0217a"/>
          </svg>
          P.O. Box 417 Redfern, OK 74990
        </p>
      </div>
    </div>

    <svg class="band__notch" viewBox="0 0 14 9" aria-hidden="true">
      <path d="M0 9 L7 0 L14 9 Z" fill="#e0217a"/>
    </svg>
    <div class="band">
      <p class="band__line">• Experience in K-12 and Higher Education • Advising and facilitating with academic skills in higher education</p>
      <p class="band__line band__line--accent">• PMB approved certification as an academic life coach</p>
    </div>
  </section>

  <section class="card card--back" aria-label="Business card, back">
    <div class="brand__mark">
      <span class="brand__dot"></span>
      <span class="brand__name">Scholarly Pathways</span>
    </div>
    <p class="back__name">Marnie Odell Fenwick</p>
    <p class="back__tagline">Educational Consultation Business</p>
  </section>

</main>
</body>
</html>
```